bluegum ridge coaching needs snazzy business card that serves a dual purpose

business card needed for a Bluegum Ridge Coaching company that takes people out on the road to teach them proficiency on their bike.
My business logo is attached. I have grey and aqua colours with my logo.
i really like bitumen/tarmac/ road in the design somehow but that is up to you.
I think navy blue will go well with my colours too. see how you go.

I want this card to look REALLY good.
the back of the card may be used for emergency contact details too
In case of Emergency I am:
Name:

Emergency Contact name
emergency contact Phone number:

• details that are essential are:
• logo
• Name: Helena FORD
• ABN: 53 291 804 667
• phone number: 0455 128 906
• chatterly logo
• * ride tuition & proficiency
• * skills practice
• * maintenance 101
• * bike fitting service
• * cater for all ages & abilities
• backpage:
• logo
• skills confidence enjoyment
• some space for writing
• nothing girly. The business will already naturally attract women, it needs to appeal to both genders

```html
<!DOCTYPE html>
<html lang="en">
<head>
<meta charset="utf-8">
<title>Bluegum Ridge Coaching – Business Card</title>
<link href="https://fonts.googleapis.com/css2?family=Lato:wght@400;700;900&display=swap" rel="stylesheet">
<style>
  :root {
    --aqua: #4bb3a2;
    --aqua-dark: #3a9c8c;
    --ink: #2b2b2b;
    --charcoal: #3a3a3a;
    --card-white: #f7f7f7;
    --alert: #ef5a55;
    --stage: #3b3b3d;
    --swoosh: #111111;
  }
  html, body {
    margin: 0;
    padding: 0;
    width: 1200px;
    height: 873px;
    overflow: hidden;
    background: var(--stage);
    font-family: "Lato", sans-serif;
  }
  .canvas {
    position: relative;
    width: 1200px;
    height: 873px;
  }
  .card {
    position: absolute;
    width: 560px;
    height: 320px;
    border-radius: 24px;
    overflow: hidden;
    background: linear-gradient(160deg, #ffffff 0%, var(--card-white) 60%, #e6e6e6 100%);
    box-shadow: 0 14px 30px rgba(0,0,0,0.45);
  }
  .card svg.card-art {
    position: absolute;
    inset: 0;
    width: 100%;
    height: 100%;
  }
  .card-back { left: 70px; top: 70px; }
  .card-front { left: 570px; top: 470px; }

  /* wordmark */
  .wordmark {
    position: absolute;
    display: flex;
    align-items: center;
    gap: 10px;
    font-weight: 700;
    letter-spacing: 0.04em;
    text-transform: uppercase;
  }
  .wordmark-dot {
    width: 26px;
    height: 26px;
    border-radius: 50%;
    background: var(--aqua);
  }
  .front-wordmark { left: 36px; top: 66px; font-size: 26px; color: var(--charcoal); line-height: 1.1; }
  .back-wordmark { left: 300px; top: 12px; font-size: 15px; color: #ffffff; }

  /* front details */
  .holder {
    position: absolute;
    right: 40px;
    top: 100px;
    text-align: right;
  }
  .holder-name { font-size: 22px; font-weight: 900; color: var(--aqua-dark); line-height: 26px; }
  .holder-role { font-size: 15px; color: var(--ink); margin-top: 2px; line-height: 18px; }
  .abn {
    position: absolute;
    right: 30px;
    top: 202px;
    font-size: 13px;
    font-weight: 700;
    color: var(--ink);
  }
  .contact-list {
    position: absolute;
    left: 30px;
    bottom: 12px;
    margin: 0;
    padding: 0;
    list-style: none;
    color: #ffffff;
    font-size: 16px;
  }
  .contact-list li { display: flex; align-items: center; gap: 10px; line-height: 22px; }
  .contact-list svg { width: 14px; height: 14px; fill: none; stroke: var(--ink); stroke-width: 2; }

  /* back details */
  .emergency {
    position: absolute;
    left: 40px;
    top: 172px;
    margin: 0;
    padding: 0;
    list-style: none;
    text-transform: uppercase;
    color: var(--ink);
  }
  .emergency-title { font-size: 17px; font-weight: 700; color: var(--alert); margin-bottom: 12px; }
  .emergency li { font-size: 13px; font-weight: 700; letter-spacing: 0.03em; margin-bottom: 16px; }
  .emergency li.field-large { font-size: 16px; }
  .faint-mark {
    position: absolute;
    right: 34px;
    bottom: 110px;
    width: 56px;
    height: 56px;
    border-radius: 50%;
    background: rgba(0,0,0,0.08);
  }
</style>
</head>
<body>
<main class="canvas">

  <!-- Back of card: emergency details -->
  <section class="card card-back" aria-label="Card back">
    <svg class="card-art" viewBox="0 0 560 320" preserveAspectRatio="none" aria-hidden="true">
      <path d="M0,0 H560 V44 C420,52 240,74 0,176 Z" fill="var(--swoosh)"/>
      <path d="M0,0 H560 V36 C420,42 240,60 0,158 Z" fill="var(--aqua)"/>
    </svg>
    <div class="wordmark back-wordmark">Bluegum Ridge Coaching</div>
    <ul class="emergency">
      <li class="emergency-title">In case of emergency</li>
      <li class="field-large">I am</li>
      <li>Emergency contact phone number:</li>
      <li>Any other information</li>
    </ul>
    <div class="faint-mark"></div>
  </section>

  <!-- Front of card -->
  <section class="card card-front" aria-label="Card front">
    <svg class="card-art" viewBox="0 0 560 320" preserveAspectRatio="none" aria-hidden="true">
      <path d="M0,200 C150,250 340,220 560,160 L560,176 C340,232 150,262 0,226 Z" fill="var(--swoosh)"/>
      <path d="M0,222 C150,256 340,226 560,172 V320 H0 Z" fill="var(--aqua)"/>
    </svg>
    <div class="wordmark front-wordmark"><span class="wordmark-dot"></span>Bluegum Ridge<br>Coaching</div>
    <div class="holder">
      <div class="holder-name">Helena FORD</div>
      <div class="holder-role">Owner / Founder</div>
    </div>
    <div class="abn">ABN: 53 291 804 667</div>
    <ul class="contact-list">
      <li><svg viewBox="0 0 14 14"><rect x="3.5" y="1" width="7" height="12" rx="1.5"/></svg>0455 128 906</li>
      <li><svg viewBox="0 0 14 14"><rect x="1" y="3" width="12" height="8" fill="var(--ink)" stroke="none"/><path d="M1,3 L7,8 L13,3" stroke="#ffffff" stroke-width="1.2"/></svg>info@bluegumridge.no</li>
      <li><svg viewBox="0 0 14 14"><path d="M5,9 L9,5 M6,3.5 L8,1.5 a2.5,2.5 0 0 1 4,4 L10,7.5 M8,10.5 L6,12.5 a2.5,2.5 0 0 1 -4,-4 L4,6.5"/></svg>www.bluegumridge.no</li>
    </ul>
  </section>

</main>
</body>
</html>
```